Menu Design for Chocolate and Cheese Shop

We are chocolate (and cheese) makers - www.mintleafery.com.au and would like to redesign our café menu (attached is the pdf of the old one). I would like to end up with a file using Adobe suite of products so we can readily update menus as we change them. Clean, classy and inviting. We would also like to incorporate our cheese with our sister business into the menu offering (www.thistledalepasture.com.au and www.facebook.com/thistledalepasture). Just allow space for us to flesh out content for the cheese menu items - we will definitely include our Brie Hour in this if you see our facebook posts) - 4pp - A4 landscape folded into A5. We would also like the exact same menu but with our Thistledale Pasture Branding instead of mintleafery (we have two different sites -attached are our thistledale pasture logos as well for incorporating into the second document)

```html
<!DOCTYPE html>
<html lang="en">
<head>
<meta charset="utf-8">
<title>mintleafery chocolate — café menu</title>
<link rel="stylesheet" href="https://fonts.googleapis.com/css2?family=Source+Sans+3:wght@400;600&family=Kalam:wght@400&display=swap">
<style>
  :root{
    --backdrop:#8f9093;
    --paper:#eae8e3;
    --band:#d7d4cd;
    --ink:#3d3632;
    --ink-soft:#544b45;
    --brand:#7a6c61;
    --brand-light:#b7aa8d;
    --photo-dark:#3a2c24;
    --photo-mid:#6b5444;
    --photo-light:#a38c78;
  }
  *{box-sizing:border-box;margin:0;padding:0}
  html,body{width:852px;height:1200px;overflow:hidden}
  body{background:var(--backdrop);font-family:"Source Sans 3",sans-serif;color:var(--ink);position:relative}
  .spread{position:absolute;left:64px;width:718px;height:507px;background:var(--paper);box-shadow:0 2px 6px rgba(0,0,0,.35);overflow:hidden}
  .spread--cover{top:71px}
  .spread--inside{top:627px}
  .spine{position:absolute;left:358px;top:0;width:2px;height:100%;background:linear-gradient(90deg,rgba(0,0,0,.08),rgba(255,255,255,.5))}
  .photo{position:absolute}
  .photo--round{width:88px;height:88px;border-radius:50%;top:56px;border:2px solid #fff;background:radial-gradient(circle at 40% 40%,var(--photo-light),var(--photo-dark))}
  .photo--strip{left:0;top:372px;width:718px;height:135px;background:linear-gradient(90deg,var(--photo-dark),var(--photo-mid) 40%,var(--photo-light) 55%,var(--photo-mid) 75%,var(--photo-dark))}
  .photo--side-left{left:0;top:0;width:104px;height:100%;background:linear-gradient(180deg,var(--photo-mid),var(--photo-light) 30%,var(--photo-dark) 70%,var(--photo-mid))}
  .photo--side-right{left:623px;top:0;width:95px;height:100%;background:linear-gradient(180deg,var(--photo-light),var(--photo-dark) 35%,var(--photo-mid) 65%,var(--photo-dark))}
  .brand{position:absolute;display:flex;align-items:center;gap:8px;color:var(--brand);font-weight:400}
  .brand__mark{border-radius:50%;background:var(--brand-light)}
  .brand--small{left:132px;top:182px;font-size:21px}
  .brand--small .brand__mark{width:18px;height:18px}
  .brand--large{left:445px;top:165px;font-size:30px}
  .brand--large .brand__mark{width:26px;height:26px}
  .contact{position:absolute;left:0;width:359px;top:240px;text-align:center;font-size:8.5px;line-height:10.5px;color:var(--ink-soft)}
  .contact p{margin-bottom:10px}
  .menu-sheet{position:absolute;top:0;height:100%;background:var(--paper)}
  .menu-sheet--left{left:104px;width:256px}
  .menu-sheet--right{left:360px;width:263px}
  .section-title{position:absolute;top:16px;height:22px;background:var(--band);font-family:"Kalam",cursive;font-size:16px;line-height:24px;padding-left:8px;color:var(--ink);font-weight:400}
  .section-title--treats{left:104px;width:256px}
  .section-title--drinks{left:362px;width:258px}
  .item{position:absolute;width:233px}
  .col-left{left:113px}
  .col-right{left:375px}
  .item__row{display:flex;align-items:baseline;font-size:11px;font-weight:600;line-height:13px;white-space:nowrap}
  .item__dots{flex:1;border-bottom:1px dotted var(--ink-soft);margin:0 3px;transform:translateY(-2px)}
  .item__price{white-space:nowrap}
  .item__desc{font-size:8.5px;line-height:10px;color:var(--ink-soft);margin-top:1px}
  .kids{position:absolute;left:113px;top:388px;width:233px;height:104px;border:1px dashed var(--ink-soft);padding:2px}
  .kids__title{background:var(--band);font-family:"Kalam",cursive;font-size:13px;line-height:20px;padding-left:6px;margin-bottom:5px;font-weight:400}
  .kids .item__row{font-size:7.5px;line-height:11px;font-weight:600;padding:0 4px}
  .cheese{position:absolute;left:392px;top:228px;width:290px}
  .cheese__title{background:var(--band);font-family:"Kalam",cursive;font-size:14px;line-height:22px;padding-left:8px;font-weight:400;margin-bottom:8px}
  .cheese .item{position:static;width:auto;margin-bottom:7px}
  .cheese__web{font-size:8px;color:var(--ink-soft);text-align:center}
</style>
</head>
<body>

<section class="spread spread--cover">
  <div class="photo photo--round" style="left:37px" role="img" aria-label="Photo of a jar of hot chocolate being served"></div>
  <div class="photo photo--round" style="left:135px" role="img" aria-label="Photo of assorted chocolates on a board"></div>
  <div class="photo photo--round" style="left:233px" role="img" aria-label="Photo of a coffee cup on a saucer"></div>

  <div class="brand brand--small"><span>mintleafery</span><span class="brand__mark"></span></div>

  <div class="contact">
    <p>14 Wattle Lane<br>Ferncastle Tasmania 7399 Australia</p>
    <p>Phone: 03 6100 4821</p>
    <p>Opening hours:<br>Mon-Fri 9:00am-5:00pm<br>Sat 9:30am-2:00pm<br>Closed - Public Holidays</p>
    <p>www.mintleaferychocolate.com.au</p>
  </div>

  <div class="brand brand--large"><span>mintleafery</span><span class="brand__mark"></span></div>

  <div class="cheese">
    <h2 class="cheese__title">Cheese from Thistledale Pasture</h2>
    <div class="item"><div class="item__row"><span>Brie Hour</span><span class="item__dots"></span><span class="item__price">$00.00</span></div><p class="item__desc">our sister farm's cheeses served with house accompaniments (details to come)</p></div>
    <div class="item"><div class="item__row"><span>Cheese plate</span><span class="item__dots"></span><span class="item__price">$00.00</span></div><p class="item__desc">space for cheese menu items to be added</p></div>
    <p class="cheese__web">www.thistledalepasture.com.au</p>
  </div>

  <div class="photo photo--strip" role="img" aria-label="Photo of chocolate slices and truffles on a wooden table"></div>
  <div class="spine"></div>
</section>

<section class="spread spread--inside">
  <div class="photo photo--side-left" role="img" aria-label="Photo of truffles and chocolate pops"></div>
  <div class="photo photo--side-right" role="img" aria-label="Photo of chocolate bars with nuts"></div>
  <div class="menu-sheet menu-sheet--left"></div>
  <div class="menu-sheet menu-sheet--right"></div>
  <div class="spine"></div>

  <h2 class="section-title section-title--treats">Sweet Treats</h2>
  <h2 class="section-title section-title--drinks">Drinks</h2>

  <div class="item col-left" style="top:61px"><div class="item__row"><span>Chocolate taste plate</span><span class="item__dots"></span><span class="item__price">$14.30</span></div><p class="item__desc">chocolate macaron, chocolate ice cream, chocolate mousse, and our signature chocolate</p></div>
  <div class="item col-left" style="top:106px"><div class="item__row"><span>Caramel taste plate</span><span class="item__dots"></span><span class="item__price">$14.30</span></div><p class="item__desc">caramel slice, hokey pokey ice cream, caramel truffle, and alfajores (Spanish shortbread) filled with dulce de leche</p></div>
  <div class="item col-left" style="top:151px"><div class="item__row"><span>Raspberry brownie</span><span class="item__dots"></span><span class="item__price">$12.50</span></div><p class="item__desc">Brownie topped with raspberries, served warm with a scoop of vanilla bean ice cream</p></div>
  <div class="item col-left" style="top:196px"><div class="item__row"><span>Ice cream sensation</span><span class="item__dots"></span><span class="item__price">$12.00</span></div><p class="item__desc">a trio of chocolate ice cream or our weekly special ice cream served with chocolate sauce and sprinkled with dark crispy pearls (ask our team what flavour is available)</p></div>
  <div class="item col-left" style="top:252px"><div class="item__row"><span>Chocolate mousse</span><span class="item__dots"></span><span class="item__price">$12.00</span></div><p class="item__desc">rich and creamy chocolate mousse served with white crispy pearls</p></div>
  <div class="item col-left" style="top:296px"><div class="item__row"><span>Handmade chocolates from:</span><span class="item__dots"></span><span class="item__price">$1.90</span></div><p class="item__desc">choose from our extensive range of fresh chocolates &amp; truffles</p></div>
  <div class="item col-left" style="top:333px"><div class="item__row"><span>Dessert jars</span><span class="item__dots"></span><span class="item__price">$15.50</span></div><p class="item__desc">ask our team to find out what is on offer this week</p></div>
  <div class="item col-left" style="top:369px"><div class="item__row"><span>Handmade cookies</span><span class="item__dots"></span><span class="item__price">$3.00</span></div></div>

  <div class="kids">
    <h3 class="kids__title">For the Children</h3>
    <div class="item__row"><span>Mini hot chocolate</span><span class="item__dots"></span><span>$3.00</span></div>
    <div class="item__row"><span>Mini chino</span><span class="item__dots"></span><span>$1.00</span></div>
    <div class="item__row"><span>Mini chino with teddy pop</span><span class="item__dots"></span><span>$2.50</span></div>
    <div class="item__row"><span>Mini ice chocolate</span><span class="item__dots"></span><span>$5.00</span></div>
    <div class="item__row"><span>Mini icecream</span><span class="item__dots"></span><span>$3.50</span></div>
    <div class="item__row"><span>Mini mousse</span><span class="item__dots"></span><span>$3.50</span></div>
  </div>

  <div class="item col-right" style="top:61px"><div class="item__row"><span>Hot chocolate</span><span class="item__dots"></span><span class="item__price">reg $5.50 – lrg $6.00</span></div><p class="item__desc">traditional – made with 65% maracaibo single origin chocolate white – made with white chocolate half and half - half traditional and half white hot chocolate</p></div>
  <div class="item col-right" style="top:113px"><div class="item__row"><span>Mocha</span><span class="item__dots"></span><span class="item__price">reg $6.00 – lrg $6.50</span></div><p class="item__desc">can be made with traditional or white chocolate</p></div>
  <div class="item col-right" style="top:148px"><div class="item__row"><span>Special hot chocolate</span><span class="item__dots"></span><span class="item__price">reg $6.50 – lrg $7.00</span></div><p class="item__desc">a creamy ganache made with crème fraiche infused with a different flavour each week (ask our team what flavour is available)</p></div>
  <div class="item col-right" style="top:202px"><div class="item__row"><span>Coffee</span><span class="item__dots"></span><span class="item__price">reg $4.00 – lrg $4.50</span></div><p class="item__desc">latte, cappuccino, flat white, long black, short black, short macchiato, long macchiato, piccolo latte</p></div>
  <div class="item col-right" style="top:248px"><div class="item__row"><span>Chai</span><span class="item__dots"></span><span class="item__price">reg $4.00 – lrg $4.50</span></div></div>
  <div class="item col-right" style="top:271px"><div class="item__row"><span>Tea - a pot of leafwell's organic tea</span><span class="item__dots"></span><span class="item__price">$5.00</span></div><p class="item__desc">english breakfast, earl grey, french earl grey, wellbeing, coconut, berry green, white tea and rose, chai, dark tea &amp; chocolate, lemongrass and ginger</p></div>
  <div class="item col-right" style="top:326px"><div class="item__row"><span>Affogato</span><span class="item__dots"></span><span class="item__price">$6.00</span></div><p class="item__desc">vanilla bean icream served with a shot of coffee or molten chocolate</p></div>
  <div class="item col-right" style="top:369px"><div class="item__row"><span>Iced coffee</span><span class="item__dots"></span><span class="item__price">$5.50</span></div></div>
  <div class="item col-right" style="top:394px"><div class="item__row"><span>Iced chocolate</span><span class="item__dots"></span><span class="item__price">$7.00</span></div><p class="item__desc">white or 65% maracaibo single origin chocolate<br>our special blend of millbrook cream, milk, and chocolate</p></div>
  <div class="item col-right" style="top:437px"><div class="item__row"><span>Iced moc ha white or traditional</span><span class="item__dots"></span><span class="item__price">$7.50</span></div></div>
  <div class="item col-right" style="top:456px"><div class="item__row"><span>Milkshakes</span><span class="item__dots"></span><span class="item__price">$6.00</span></div><p class="item__desc">chocolate, (our own decadent fudge, vanilla or caramel)</p></div>
  <div class="item col-right" style="top:487px"><div class="item__row"><span>Glenvale – still or sparkling water</span><span class="item__dots"></span><span class="item__price">$3.00</span></div></div>
</section>

</body>
</html>
```